Stationery + Biz Cards for an online geek store
Vicente Moraes
Stationery + Biz Cards for an online geek store - Hobbies
Creative Brief
Use same font as used in my logo
Try to use the same font if possible
Professional
General Manager
Rua Benedita, 542 - casa 11, 04317-020 - São Paulo - SP
vicente.moraes@nerdpraca.com.br
www.nerdpraca.com.br
Logo + Website www.nerdpraca.com.br

```html
<!DOCTYPE html>
<html lang="pt-BR">
<head>
<meta charset="utf-8">
<title>nerdpraca – Business Cards</title>
<link rel="stylesheet" href="https://fonts.googleapis.com/css2?family=Open+Sans:wght@400;600;700&display=swap">
<style>
  :root {
    --page: #e6e3de;
    --card-dark: #1c1c1c;
    --card-dark-top: #4a4e52;
    --card-dark-mid: #2a2d30;
    --card-light: #f4f4f4;
    --card-light-edge: #d9d9d9;
    --green: #8cc63f;
    --green-dark: #6ea52c;
    --white: #ffffff;
    --text: #4a4a4a;
    --muted: #6b6b6b;
  }
  * { box-sizing: border-box; margin: 0; padding: 0; }
  html, body {
    width: 1200px; height: 899px; overflow: hidden;
    background: var(--page);
    font-family: "Open Sans", Arial, sans-serif;
  }
  .canvas { position: relative; width: 1200px; height: 899px; }

  .card {
    position: absolute;
    overflow: hidden;
    box-shadow: 0 6px 18px rgba(0,0,0,0.25);
  }

  /* Front card */
  .card-front { left: 73px; top: 75px; width: 535px; height: 335px; background: linear-gradient(180deg, var(--card-light) 60%, var(--card-light-edge)); }
  .front-header {
    position: absolute; left: 0; top: 0; width: 100%; height: 155px;
    background: radial-gradient(ellipse at 50% 0%, var(--card-dark-top), var(--card-dark-mid) 55%, var(--card-dark) 100%);
    display: flex; align-items: center; justify-content: center;
    border-bottom: 3px solid #111;
  }
  .brand { display: flex; align-items: center; gap: 14px; }
  .brand-dot { width: 34px; height: 34px; border-radius: 50%; background: var(--green); }
  .brand-name { font-weight: 700; color: var(--white); letter-spacing: -1px; }
  .front-header .brand-name { font-size: 46px; }

  .person { position: absolute; left: 20px; top: 180px; }
  .person-name { color: var(--green-dark); font-weight: 700; font-size: 15px; }
  .person-role { color: var(--text); font-size: 13px; margin-top: 1px; }

  .contacts { position: absolute; left: 318px; top: 178px; list-style: none; }
  .contacts li { display: flex; align-items: flex-start; gap: 8px; font-size: 10.5px; color: var(--muted); line-height: 14px; margin-bottom: 5px; }
  .contacts .icon { flex: none; width: 11px; height: 11px; margin-top: 1px; border-radius: 50%; background: var(--green); }

  /* Back card */
  .card-back { left: 607px; top: 510px; width: 566px; height: 323px; background: var(--card-dark); }
  .back-logo { position: absolute; left: 0; top: 0; width: 100%; height: 250px; display: flex; align-items: center; justify-content: center; }
  .card-back .brand-name { font-size: 58px; color: var(--green); }
  .card-back .brand-dot { width: 42px; height: 42px; }
  .back-band { position: absolute; left: 0; bottom: 0; width: 100%; height: 40px; }
</style>
</head>
<body>
<main class="canvas">

  <section class="card card-front" aria-label="Business card front">
    <header class="front-header">
      <div class="brand">
        <span class="brand-dot"></span>
        <span class="brand-name">nerdpraca</span>
      </div>
    </header>

    <div class="person">
      <p class="person-name">Vicente Moraes</p>
      <p class="person-role">General Manager</p>
    </div>

    <ul class="contacts">
      <li><span class="icon"></span><span>Rua Benedita, 542 - casa 11,<br>04317-020 - São Paulo - SP</span></li>
      <li><span class="icon"></span><span>+55 11 3174-2260</span></li>
      <li><span class="icon"></span><span>+55 11 9-8531-6042</span></li>
      <li><span class="icon"></span><span>vicente.moraes@nerdpraca.com.br</span></li>
      <li><span class="icon"></span><span>www.nerdpraca.com.br</span></li>
    </ul>
  </section>

  <section class="card card-back" aria-label="Business card back">
    <div class="back-logo">
      <div class="brand">
        <span class="brand-dot"></span>
        <span class="brand-name">nerdpraca</span>
      </div>
    </div>
    <svg class="back-band" viewBox="0 0 566 40" preserveAspectRatio="none" aria-hidden="true">
      <polygon points="0,4 430,4 410,26 0,26" fill="#8cc63f"/>
      <polygon points="410,26 430,4 566,4 566,26" fill="#2b2b2b"/>
      <rect x="0" y="26" width="566" height="14" fill="#111"/>
    </svg>
  </section>

</main>
</body>
</html>
```